Zielgruppe
Wir sind eine Kellerei, die Weine für den Groß-, Fach- und Online-Handel produziert.
Unsere Zielgruppe ist bei diesem Produkt eine Käuferschaft, die am Thema Genuss & Wein interessiert ist.
Titel:
Glühwein rot und weiß
Aufgabe:
Moderniesieren des Design mit Wiedererkennungsfaktor von bestehendem Produkt.
Druck Vorder- und Rückenetikett für Glühwein rot und weiß
(Unser Produkt wurde druch einen Mitbewerber kopiert und im Handel platziert [Bild Replika]. Das neue Design soll sich klar abgrenzen, aber für den Kunden einen Wiedererkennungswert haben)
Aufgabenstellung
Druck:
4c - eventuell mit Veredelung (Heißfolie gold oder Lack)
Ob 1 oder 2 getrennte Eitketten für Motiv + Lebensmittelrechtliche Angaben steht offen
Wichtig:
Platz für Pflichtangaben Wein + EAN-Code
Kapsel:
Schraubverschluss einfarbig ohne Aufdruck
Etikett:
Format für Motiv: Höhe bis 80mm Breite bis 150 mm
Flaschenform:
Bordeauxflasche dunkel (siehe altes Produkt)

```html
<!DOCTYPE html>
<html lang="de">
<head>
<meta charset="utf-8">
<title>Glühwein rot – Etikett</title>
<link rel="stylesheet" href="https://fonts.googleapis.com/css2?family=Abril+Fatface&display=swap">
<style>
  :root {
    --stage: #5a5a5a;
    --label: #141414;
    --label-top: #1c1c1c;
    --ink-light: #f3f3f1;
    --accent: #c2164c;
  }
  html, body {
    margin: 0;
    padding: 0;
    width: 1200px;
    height: 790px;
    overflow: hidden;
    background: var(--stage);
  }
  .canvas {
    position: relative;
    width: 1200px;
    height: 790px;
    background: radial-gradient(ellipse at 50% 50%, #8a8a8a 0%, #5a5a5a 55%, #3c3c3c 100%);
  }
  .label {
    position: absolute;
    left: 393px;
    top: 45px;
    width: 414px;
    height: 700px;
    display: block;
  }
  .wordmark {
    font-family: "Abril Fatface", serif;
    fill: var(--ink-light);
  }
  .variety {
    font-family: "Abril Fatface", serif;
    fill: var(--accent);
  }
  .thread {
    stroke: var(--accent);
    stroke-width: 1;
    fill: none;
  }
  .producer {
    font-family: "Abril Fatface", serif;
    fill: var(--ink-light);
    letter-spacing: 0.5px;
  }
  .producer-mark {
    fill: none;
    stroke: var(--ink-light);
    stroke-width: 0.8;
  }
</style>
</head>
<body>
<main class="canvas">
  <svg class="label" viewBox="0 0 280 474" xmlns="http://www.w3.org/2000/svg" aria-label="Etikett Glühwein rot">
    <defs>
      <clipPath id="label-edge">
        <rect x="0" y="0" width="280" height="474"/>
      </clipPath>
      <linearGradient id="label-surface" x1="0" y1="0" x2="0" y2="1">
        <stop offset="0" stop-color="var(--label-top)"/>
        <stop offset="1" stop-color="var(--label)"/>
      </linearGradient>
    </defs>
    <rect class="label-ground" x="0" y="0" width="280" height="474" fill="url(#label-surface)"/>
    <g clip-path="url(#label-edge)">
      <g class="title" transform="rotate(4 140 170)">
        <text class="wordmark" x="26" y="148" font-size="96" letter-spacing="-3">glüh</text>
        <text class="wordmark" x="86" y="222" font-size="96" letter-spacing="-3">wein</text>
      </g>
      <text class="variety" x="122" y="304" font-size="56" letter-spacing="-1" transform="rotate(4 160 290)">rot</text>
      <line class="thread" x1="0" y1="282" x2="280" y2="334"/>
      <line class="thread" x1="0" y1="389" x2="280" y2="290"/>
    </g>
    <g class="producer-lockup">
      <text class="producer" x="128" y="417" font-size="15" text-anchor="middle">HALVERN</text>
      <rect class="producer-mark" x="178" y="404" width="13" height="13"/>
    </g>
  </svg>
</main>
</body>
</html>
```